Business Card 85x40mm - Freelance audio mixing / live event operator

I am a freelance audio operator working in live events. Mostly corporate events mixing sound for a range of entertainment, awards nights and functions. I need a new card to give to perspective clients.

The final design will convey bold professionalism with a general dark vibe. Looking for dark-ish background with some smatterings of colour added.

I have attatched my old BC for an idea of what I have liked in the past. Id like a more modern updated design (that circular design on the back is not my logo it is just a picture I found that resembled sound} . For an added element possibly a mixture of some playful colours in a way that resembles an audio wave form or sound.

I have attached a photo called "audio software" with some colourful squiggly lines; maybe incorporate elements of that into into design
Updates

Added extra $ to project Damn Pixel herds fees are unreasonable

Target Market(s)

Mostly corporate clients

Industry/Entity Type

Events

Contact Information for Business Card

Corwin Blaylock
Sound | FOH | Monitors | Systems | Corporate

Digital Audio Mixing Specialist, Live Event Technical Professional,

corwinblaylock@mailvane.net, +61 408 315 927

Colors
ec1f27
ffc214
9bcb3c
6b449b

Requirements
Must have
• Dark theme
• 85x40mm dimensions
Nice to have
• some sort of imagery or design to reflect audio/sound

```html
<!DOCTYPE html>
<html lang="en">
<head>
<meta charset="utf-8">
<title>Corwin Blaylock – Business Card</title>
<link href="https://fonts.googleapis.com/css2?family=Arimo:wght@400;700&display=swap" rel="stylesheet">
<style>
  :root {
    --ink: #120d0e;
    --card: #1a1314;
    --card-edge: #2a2122;
    --stage: #3a2a1c;
    --green: #8cc63f;
    --orange: #f7821f;
    --yellow: #ffc214;
    --grey: #6d6a6a;
    --grid: rgba(255,255,255,0.05);
  }
  * { margin: 0; padding: 0; box-sizing: border-box; }
  html, body { width: 1200px; height: 1200px; overflow: hidden; }
  body {
    font-family: "Arimo", Arial, sans-serif;
    background: var(--stage);
    position: relative;
  }
  .brand-band {
    position: absolute; left: 0; top: 0;
    width: 1200px; height: 330px;
    background: var(--ink);
    display: flex; align-items: center; justify-content: center;
  }
  .wordmark {
    display: flex; align-items: center; gap: 22px;
    color: var(--green);
    font-weight: 700;
    font-size: 64px;
    letter-spacing: 1px;
  }
  .wordmark .mark-square {
    width: 44px; height: 44px;
    background: var(--orange);
  }
  .card {
    position: absolute; left: 220px;
    width: 760px; height: 358px;
    background: linear-gradient(160deg, #2a2021 0%, var(--card) 45%, #070505 100%);
    border: 1px solid var(--card-edge);
    box-shadow: 0 18px 40px rgba(0,0,0,0.55);
    overflow: hidden;
  }
  .card--front { top: 372px; }
  .card--back { top: 790px; }

  .grid-lines { position: absolute; inset: 0; }
  .waveform {
    position: absolute; left: 120px; right: 40px; top: 70px; height: 190px;
    background: radial-gradient(ellipse at 45% 60%, rgba(150,150,150,0.45) 0%, rgba(70,80,110,0.25) 40%, rgba(0,0,0,0) 72%);
  }
  .front-mark {
    position: absolute; left: 0; right: 0; top: 120px;
    display: flex; justify-content: center;
  }
  .front-mark .wordmark { font-size: 46px; gap: 16px; }
  .front-mark .mark-square { width: 32px; height: 32px; }
  .services {
    position: absolute; left: 0; right: 0; bottom: 54px;
    text-align: center;
    color: var(--green);
    font-size: 21px;
    letter-spacing: 0.5px;
  }

  .back-mark {
    position: absolute; left: 40px; top: 112px; width: 300px;
    display: flex; justify-content: center;
  }
  .back-mark .wordmark { font-size: 30px; gap: 12px; }
  .back-mark .mark-square { width: 22px; height: 22px; }
  .divider {
    position: absolute; left: 372px; top: 44px;
    width: 1px; height: 190px;
    background: linear-gradient(to bottom, rgba(247,130,31,0), var(--orange), rgba(247,130,31,0));
  }
  .contact {
    position: absolute; left: 410px; top: 70px;
    color: var(--orange);
  }
  .contact .name { font-size: 28px; font-weight: 700; margin-bottom: 26px; }
  .contact .line { font-size: 18px; margin-bottom: 10px; }
  .role {
    position: absolute; left: 0; right: 0; bottom: 40px;
    text-align: center;
    color: var(--green);
    font-size: 20px;
  }
</style>
</head>
<body>
  <header class="brand-band">
    <div class="wordmark"><span class="mark-square"></span>Corwin Blaylock</div>
  </header>

  <section class="card card--front">
    <svg class="grid-lines" width="760" height="358" aria-hidden="true">
      <g stroke="rgba(255,255,255,0.05)" stroke-width="1">
        <line x1="0" y1="60" x2="760" y2="60"/><line x1="0" y1="120" x2="760" y2="120"/>
        <line x1="0" y1="180" x2="760" y2="180"/><line x1="0" y1="240" x2="760" y2="240"/>
        <line x1="100" y1="0" x2="100" y2="358"/><line x1="220" y1="0" x2="220" y2="358"/>
        <line x1="340" y1="0" x2="340" y2="358"/><line x1="460" y1="0" x2="460" y2="358"/>
        <line x1="580" y1="0" x2="580" y2="358"/><line x1="700" y1="0" x2="700" y2="358"/>
      </g>
    </svg>
    <div class="waveform" role="img" aria-label="Grey audio waveform sweeping across the card"></div>
    <div class="front-mark">
      <div class="wordmark"><span class="mark-square"></span>Corwin Blaylock</div>
    </div>
    <p class="services">Sound | FOH | Monitors | Systems | Corporate</p>
  </section>

  <section class="card card--back">
    <div class="back-mark">
      <div class="wordmark"><span class="mark-square"></span>Corwin Blaylock</div>
    </div>
    <div class="divider"></div>
    <div class="contact">
      <p class="name">Corwin Blaylock</p>
      <p class="line">+61 408 315 927</p>
      <p class="line">corwinblaylock@mailvane.net</p>
    </div>
    <p class="role">Digital Audio Mixing Specialist - Live Event Technical Professional</p>
  </section>
</body>
</html>
```